Private Gym Needs a Rack Card Design

We need a basic front and back rack card (same size as post card) that gives basic information about our brand, and includes our logo. Please see attached logo and required content below.

Target Market(s)

Upscale, private gym.

Industry/Entity Type

Gym

Font styles to use
Sans Serif

Colors
ffffff
5c5c5c
000000
dbdbdb
f78f20

Requirements
Must have
• Business Logo and the following text in a clean, modern, easy-to-read, artistic manner. Style and design must be clean, incorporate our color scheme of MOSTLY white, light grey, charcoal, with just pops of orange. We want the card itself to be mostly white background. Must include website URL as well: corevantagestudio.com
• FRONT CARD:
• Logo
• A safe and individualized approach to exercise
• Our method employs the latest weight resistance training exercises and coaching for healthy living. Not only is our workout methodology effective, it’s safe.
• Our Method…
• -Improves Functional Movement
• -Promotes Weight Loss
• -Builds Strength
• -Increases Flexibility 

• BACK:
• Change Your Body. Find Your Strength.
• There’s 40 years of success behind our proven method
• What is The Formwell? 
• The Formwell is all about teaching our clients how to lift weights and exercise with the proper technique. There’s no slinging or jerking at our gym; only controlled movements that yield real results.
• Come workout with us in our private gym. We are located in Durham adjacent to Harlow Campus and 5 minutes from downtown Durham.
• Address: 482 Linden Ave, Durham, NC 27705
• Phone: (919) 555-2741
• Hours: 9:00 AM – 9:00 PM
Nice to have
• Great organization of text, maybe some columns, colored bullet points, cool graphics and logos.
Should not have
• Busy or crowded design. All lines should be sleek, straight, and streamline. NO STOCK IMAGES, but logos are GREAT

```html
<!DOCTYPE html>
<html lang="en">
<head>
<meta charset="utf-8">
<title>The Formwell – Rack Card</title>
<link href="https://fonts.googleapis.com/css2?family=Roboto+Condensed:wght@700&family=Open+Sans:wght@300;400;600&family=Nunito:wght@900&family=Dancing+Script:wght@500&display=swap" rel="stylesheet">
<style>
  :root{
    --backdrop:#744a2b;
    --charcoal-dark:#1f1f1f;
    --charcoal:#3a3a3a;
    --steel:#5c5c5c;
    --light-grey:#dbdbdb;
    --white:#ffffff;
    --orange:#f78f20;
    --orange-text:#ee6a2c;
    --headline-yellow:#f7c315;
    --black:#000000;
  }
  *{box-sizing:border-box;margin:0;padding:0}
  html,body{width:1200px;height:1155px;overflow:hidden;background:var(--backdrop)}
  body{position:relative;font-family:"Open Sans",sans-serif}

  .card{position:absolute;top:123px;width:449px;height:952px;overflow:hidden;
        box-shadow:4px 5px 8px rgba(0,0,0,.45);background:var(--white)}
  .card--front{left:106px}
  .card--back{left:625px}

  .card__header{position:absolute;left:0;top:0;width:100%;height:115px;
        background:linear-gradient(180deg,#151515 0%,#2c2c2c 55%,#4a4a4a 100%);
        display:flex;flex-direction:column;justify-content:center;align-items:center}
  .card__headline{font-family:"Roboto Condensed",sans-serif;font-weight:700;color:var(--headline-yellow);
        font-size:34px;line-height:43px;text-align:center;letter-spacing:.3px;
        text-shadow:1px 2px 2px rgba(0,0,0,.7)}
  .card__rule{position:absolute;left:0;top:115px;width:100%;height:8px;
        background:linear-gradient(180deg,#e6e6e6,#9a9a9a)}
  .card__photo{position:absolute;left:0;top:123px;width:100%;height:358px}
  .card--front .card__photo{background:linear-gradient(180deg,#9cc3e0 0%,#eef2f5 35%,#d7dde4 70%,#f2f2f2 100%)}
  .card--back .card__photo{background:linear-gradient(180deg,#f4f6f7 0%,#cfd8d6 45%,#b9c6c0 60%,#eceeef 80%,#dfe3ea 100%)}

  /* front */
  .front__panel{position:absolute;left:0;top:481px;width:100%;height:275px;
        background:linear-gradient(180deg,#2d2d2d 0%,#4a4a4a 50%,#2e2e2e 100%)}
  .front__intro{position:absolute;top:12px;left:20px;right:20px;text-align:center;
        color:#e8e8e8;font-size:15px;line-height:24px}
  .front__method{position:absolute;top:116px;width:100%;text-align:center;
        font-family:"Dancing Script",cursive;color:var(--orange);font-size:21px;line-height:28px}
  .front__benefits{position:absolute;top:151px;left:0;width:100%;list-style:none}
  .front__benefits li{height:28px;margin-bottom:3px;text-align:center;color:var(--white);
        font-size:17.5px;line-height:28px;letter-spacing:.2px;
        background:linear-gradient(180deg,#6a6a6a 0%,#4a4a4a 45%,#3a3a3a 100%)}
  .front__footer{position:absolute;left:0;top:756px;width:100%;height:196px;background:var(--white);text-align:center}
  .brand{display:flex;align-items:center;justify-content:center;gap:10px;margin-top:26px}
  .brand__mark{width:22px;height:22px;background:var(--orange)}
  .brand__name{font-family:"Open Sans",sans-serif;font-weight:600;font-size:34px;color:var(--steel);letter-spacing:.5px}
  .front__call{margin-top:24px;font-family:"Nunito",sans-serif;font-weight:900;font-size:29px;color:var(--orange-text);letter-spacing:.5px}
  .front__web{margin-top:2px;font-size:23px;color:var(--steel);letter-spacing:1.5px}

  /* back */
  .back__panel{position:absolute;left:0;top:481px;width:100%;height:353px;
        background:linear-gradient(180deg,#3a3a3a 0%,#2b2b2b 60%,#262626 100%)}
  .back__infobox{position:absolute;left:28px;top:43px;width:387px;height:270px;
        background:var(--orange);border:1.5px solid #ffe3c0;border-radius:0 4px 10px 4px;
        box-shadow:2px 3px 6px rgba(0,0,0,.5);padding:12px 22px 0 20px;color:var(--black)}
  .back__title{text-align:center;font-weight:400;font-size:20px;line-height:26px}
  .back__body{margin-top:8px;font-size:13.4px;line-height:21px;text-align:justify}
  .back__proof{margin-top:8px;color:var(--white);font-weight:300;font-size:27px;line-height:34px}
  .back__address{margin-top:10px;font-size:20px;line-height:28px;white-space:nowrap}
  .back__footer{position:absolute;left:0;top:834px;width:100%;height:118px;
        background:linear-gradient(180deg,#9a9a9a 0%,#5e5e5e 25%,#4a4a4a 100%);text-align:center;color:var(--white)}
  .back__phone{margin-top:20px;font-weight:600;font-size:43px;line-height:50px;text-shadow:1px 2px 3px rgba(0,0,0,.6)}
  .back__hours{margin-top:2px;font-size:23px}
</style>
</head>
<body>

<section class="card card--front">
  <header class="card__header">
    <h1 class="card__headline">A Safe And Individualized<br>Approach To Exercise</h1>
  </header>
  <div class="card__rule"></div>
  <div class="card__photo" role="img" aria-label="Group of people exercising with dumbbells while seated on blue exercise balls in a bright studio"></div>
  <div class="front__panel">
    <p class="front__intro">Our Method Employs<br>The Latest Weight Resistance Training Exercises And Coaching For Healthy Living. Not Only Is Our Workout Methodology Effective, It's Safe.</p>
    <p class="front__method">Our Method...</p>
    <ul class="front__benefits">
      <li>IMPROVES FUNCTIONAL MOVEMENT</li>
      <li>PROMOTES WEIGHT LOSS</li>
      <li>BUILDS STRENGTH</li>
      <li>INCREASES FLEXIBILITY</li>
    </ul>
  </div>
  <footer class="front__footer">
    <div class="brand"><span class="brand__mark"></span><span class="brand__name">The Formwell</span></div>
    <p class="front__call">Call Us: (919) 555-2741</p>
    <p class="front__web">www.corevantagestudio.com</p>
  </footer>
</section>

<section class="card card--back">
  <header class="card__header">
    <h1 class="card__headline">Change Your Body<br>Find Your Strength</h1>
  </header>
  <div class="card__rule"></div>
  <div class="card__photo" role="img" aria-label="Three women doing a floor stretch on yoga mats in a studio with large windows"></div>
  <div class="back__panel">
    <div class="back__infobox">
      <h2 class="back__title">What is the FORMWELL?</h2>
      <p class="back__body">The Formwell is all about teaching our clients how to lift weights and exercise with the proper technique. There's no slinging or jerking at our gym; only controlled movements that yield real results.</p>
      <p class="back__proof">There's 40 YEARS of success behind our proven method</p>
      <p class="back__address">482 Linden Ave, Durham, NC 27705</p>
    </div>
  </div>
  <footer class="back__footer">
    <p class="back__phone">(919) 555-2741</p>
    <p class="back__hours">Hours: 9:00 AM – 9:00 PM</p>
  </footer>
</section>

</body>
</html>
```